Salon Signage

We need a new company sign designed for the exterior of our salon. I have attached our current logos for an idea. I have also attached a photo of what salon looks like currently.

```html
<!DOCTYPE html>
<html lang="en">
<head>
<meta charset="utf-8">
<title>Glossway Beauty Salon – Exterior Sign</title>
<link href="https://fonts.googleapis.com/css2?family=Montserrat:wght@700;800;900&family=Allura&display=swap" rel="stylesheet">
<style>
  :root {
    --stage: #7a7a7a;
    --pink-deep: #f6b0c1;
    --pink-soft: #fde4ea;
    --white: #ffffff;
    --plum: #a0218a;
    --ink: #0b0b0b;
    --hair-dark: #4a2a24;
    --hair-mid: #7a4a3e;
    --skin: #e9c6b5;
  }
  * { margin: 0; padding: 0; box-sizing: border-box; }
  html, body {
    width: 1200px; height: 1200px; overflow: hidden;
    background: var(--stage);
  }
  .sign {
    position: absolute;
    left: 53px; top: 418px;
    width: 1095px; height: 363px;
    overflow: hidden;
    background: radial-gradient(ellipse 420px 260px at 520px 210px, var(--white) 0%, var(--pink-soft) 45%, var(--pink-deep) 100%);
    font-family: "Montserrat", Arial, sans-serif;
  }
  .sign__stripe {
    position: absolute; left: 222px; right: 0; top: 0;
    height: 10px; background: var(--plum);
  }
  .sign__photo {
    position: absolute; left: 0; top: 0; bottom: 0; width: 300px;
    background:
      linear-gradient(90deg, rgba(246,176,193,0) 75%, var(--pink-deep) 100%),
      linear-gradient(160deg, var(--hair-mid) 0%, var(--hair-dark) 45%, var(--skin) 70%, var(--hair-dark) 100%);
  }
  .brand__mark {
    position: absolute; left: 330px; top: 40px;
    width: 150px; height: 150px; border-radius: 50%;
    background: var(--plum);
  }
  .brand__name {
    position: absolute; left: 490px; top: 30px;
    font-weight: 900; font-size: 94px; line-height: 1;
    letter-spacing: -1px; color: var(--ink);
  }
  .brand__tagline {
    position: absolute; left: 700px; top: 122px;
    font-family: "Allura", cursive;
    font-size: 74px; line-height: 1; color: var(--ink);
  }
  .services {
    position: absolute; left: 323px; top: 293px;
    display: flex; align-items: center; height: 52px;
  }
  .services__tag {
    height: 52px; display: flex; align-items: center;
    padding: 0 10px; color: var(--white);
    font-weight: 800; font-size: 38px; letter-spacing: 0.5px;
  }
  .services__tag--hair { background: var(--ink); width: 137px; }
  .services__tag--beauty { background: var(--plum); width: 230px; padding-left: 14px; }
  .services__amp {
    position: relative; z-index: 1;
    margin: -18px -10px 0 -4px;
    font-weight: 900; font-size: 66px; line-height: 1;
    color: var(--white);
    -webkit-text-stroke: 2px var(--ink);
  }
  .contact {
    position: absolute; left: 770px; top: 296px;
    display: flex; align-items: center; gap: 10px;
  }
  .contact__icon { width: 36px; height: 36px; }
  .contact__number {
    font-weight: 800; font-size: 44px; line-height: 1; color: var(--ink);
  }
</style>
</head>
<body>
  <section class="sign">
    <div class="sign__stripe"></div>
    <div class="sign__photo" role="img" aria-label="Photograph of a woman in profile with long glossy brown hair"></div>

    <div class="brand__mark"></div>
    <h1 class="brand__name">GLOSSWAY</h1>
    <p class="brand__tagline">Beauty Salon</p>

    <div class="services">
      <span class="services__tag services__tag--hair">HAIR</span>
      <span class="services__amp">&amp;</span>
      <span class="services__tag services__tag--beauty">BEAUTY</span>
    </div>

    <div class="contact">
      <svg class="contact__icon" viewBox="0 0 36 36" aria-hidden="true">
        <path d="M8 6c2-1 3 0 4 2l2 4c1 2 0 3-1 4l-1 1c1 3 4 6 7 7l1-1c1-1 2-2 4-1l4 2c2 1 3 2 2 4l-1 2c-1 2-3 3-6 2C14 30 6 22 4 13c-1-3 0-5 2-6z" fill="#a0218a"/>
        <path d="M21 5a10 10 0 0 1 10 10M21 10a5 5 0 0 1 5 5" stroke="#a0218a" stroke-width="2.4" fill="none" stroke-linecap="round"/>
      </svg>
      <span class="contact__number">9140 3257</span>
    </div>
  </section>
</body>
</html>
```